One of a kind, 100% Pure & Natural Skincare line needs stunning product label

We need product label design for new natural skincare company called Milo & Tess Skincare. We create luxurious, 100% pure & natural skincare that is free from ingredients that may be potentially irritating to the skin. No toxins, preservatives or additives. Our initial product is Harbor Glow Balm, a nourishing face cream that suits discerning women with mature skin and those with dry/sensitive skin needing extra hydration. Also those that choose to minimize their exposure to environmental toxins. Our brand is simple yet elegant, supporting a holistic, authentic lifestyle and embracing natural skincare.

Target Market(s)

Discerning women with mature skin and those with dry/sensitive skin needing extra hydration. Also those that choose to minimize their exposure to environmental toxins.

Industry/Entity Type

Skin Care Product

Font styles to use
Sans Serif
Script

Colors
f9d9e8
fef1ee

Requirements
Must have
• The Logo.
HARBOR GLOW BALM
EMBRACING NATURAL SKINCARE
Labels must be feminine, simple/minimal yet stylish. Uncluttered yet elegant.
This is a very natural product with minimal ingredients.
Nice to have
• The logo can be incorporated in to the label, or It can be left separate as a sticker on top of the jar. The product is a firm balm consistency and is in frosted glass jars with matt silver lids.
Jar height is 45mm, width is 60mm.
Label height: 28mm and length 185mm
Should not have
• Natural or farmers market type theme. No Bold/loud lettering.

```html
<!DOCTYPE html>
<html lang="en">
<head>
<meta charset="utf-8">
<title>Harbor Glow Balm – Label</title>
<link rel="stylesheet" href="https://fonts.googleapis.com/css2?family=Great+Vibes&family=Montserrat:wght@400;600&display=swap">
<style>
  :root {
    --page-bg: #ffffff;
    --dieline: #bfe0ee;
    --label-edge: #8c8c8c;
    --blush: #f4bccb;
    --blush-soft: #f9d9e8;
    --petal: #fdf3f6;
    --ink: #2b2b2b;
    --ink-soft: #555555;
    --muted: #8a8a8a;
  }
  html, body {
    margin: 0;
    padding: 0;
    width: 1200px;
    height: 1000px;
    overflow: hidden;
    background: var(--page-bg);
    font-family: "Montserrat", Arial, sans-serif;
    color: var(--ink);
  }
  .dieline {
    position: absolute;
    left: 41px;
    top: 398px;
    width: 1134px;
    height: 203px;
    border: 1px dashed var(--dieline);
    box-sizing: border-box;
  }
  .label {
    position: absolute;
    left: 19px;
    top: 17px;
    width: 1097px;
    height: 167px;
    border: 1px solid var(--label-edge);
    box-sizing: border-box;
    background: linear-gradient(90deg, #ffffff 0, #ffffff 360px, var(--blush-soft) 620px, var(--blush) 747px, #ffffff 747px, #ffffff 100%);
  }
  .safe-area {
    position: absolute;
    left: 19px;
    top: 18px;
    width: 1057px;
    height: 129px;
    border: 1px dashed var(--dieline);
    box-sizing: border-box;
  }
  .panel p {
    position: absolute;
    margin: 0;
    font-size: 10px;
    line-height: 13px;
  }
  .panel strong { font-weight: 600; letter-spacing: 0.3px; }
  .panel--info .ingredients { left: 24px; top: 24px; width: 290px; }
  .panel--info .directions { left: 24px; top: 67px; width: 250px; }
  .panel--info .allergy { left: 24px; top: 110px; width: 320px; }
  .panel--care .caution { left: 754px; top: 24px; width: 320px; }
  .panel--care .storage { left: 754px; top: 68px; }
  .panel--care .origin { left: 754px; top: 91px; }
  .panel--care .batch { left: 754px; top: 109px; }
  .panel--care .contact {
    left: 754px;
    top: 129px;
    display: flex;
    align-items: center;
    gap: 4px;
  }
  .shelf-life {
    position: absolute;
    left: 1040px;
    top: 120px;
  }
  .brand-name {
    position: absolute;
    left: 338px;
    top: 84px;
    font-family: "Great Vibes", cursive;
    font-size: 15px;
    line-height: 18px;
    color: var(--ink);
    white-space: nowrap;
    display: flex;
    align-items: center;
    gap: 5px;
  }
  .brand-dot {
    width: 8px;
    height: 8px;
    border-radius: 50%;
    background: var(--blush);
  }
  .flower-mark {
    position: absolute;
    left: 596px;
    top: 32px;
    width: 36px;
    height: 36px;
    border-radius: 50%;
    background: var(--petal);
  }
  .product-title {
    position: absolute;
    left: 490px;
    top: 66px;
    width: 250px;
    text-align: center;
    font-family: "Great Vibes", cursive;
    font-size: 28px;
    line-height: 34px;
    color: var(--ink);
    margin: 0;
    font-weight: 400;
  }
  .tagline {
    position: absolute;
    left: 490px;
    top: 102px;
    width: 250px;
    text-align: center;
    font-size: 8px;
    letter-spacing: 0.6px;
    color: var(--muted);
  }
  .net-weight {
    position: absolute;
    left: 525px;
    top: 135px;
    font-size: 6px;
    color: var(--ink-soft);
  }
</style>
</head>
<body>
  <div class="dieline">
    <div class="label">
      <div class="safe-area"></div>

      <section class="panel panel--info">
        <p class="ingredients"><strong>INGREDIENTS :</strong> Tallow from pasture raised goats, frankincense, sandalwood &amp; myrrh essential oils.</p>
        <p class="directions"><strong>DIRECTIONS :</strong> Soften small amount in palm of hand &amp; gently massage into skin as often as</p>
        <p class="allergy">Allergy patch test recommended. If irritation occurs, discon-tinue use.</p>
      </section>

      <div class="brand-name"><span class="brand-dot"></span>Milo &amp; Tess Skincare</div>
      <div class="flower-mark" role="img" aria-label="Small white flower motif"></div>
      <h1 class="product-title">Harbor Glow Balm</h1>
      <div class="tagline">EMBRACING NATURAL SKINCARE</div>
      <div class="net-weight">NET WT 1.76 oz</div>

      <section class="panel panel--care">
        <p class="caution"><strong>CAUTION:</strong> Keep out of reach of children. If pregnant or breastfeeding, consult your healthcare practitioner. Avoid contact with eyes &amp; sensitive areas.</p>
        <p class="storage">Store below 25°C</p>
        <p class="origin">MADE IN AUSTRALIA</p>
        <p class="batch">B#</p>
        <p class="contact">
          <svg width="13" height="9" viewBox="0 0 13 9" aria-hidden="true"><rect x="0.5" y="0.5" width="12" height="8" fill="none" stroke="#2b2b2b"/><path d="M0.5 0.5 L6.5 5 L12.5 0.5" fill="none" stroke="#2b2b2b"/></svg>
          info@milotessskincare.example
        </p>
      </section>

      <svg class="shelf-life" width="24" height="20" viewBox="0 0 24 20" aria-label="Period after opening: 6 months" role="img">
        <path d="M3 8 L21 8 L21 18 L3 18 Z" fill="none" stroke="#2b2b2b" stroke-width="1"/>
        <path d="M3 8 L5 2 L19 4" fill="none" stroke="#2b2b2b" stroke-width="1"/>
        <text x="12" y="16" font-size="5.5" text-anchor="middle" font-family="Montserrat, Arial, sans-serif" font-weight="600" fill="#2b2b2b">6M</text>
      </svg>
    </div>
  </div>
</body>
</html>
```